Banner to celebrate Pellister Journeys 40 years in business. Will be used on our social media channels.

Hello
We would like a banner created to celebrate 40 years in business with tagline "service through experience since 1983"
also add our website pellisterjourneys.com.au
Banner size must be : 650 x 150px
open to suggestions

Target Market(s)

current and prospective clients

Industry/Entity Type

Travel & Tourism (Business Travel)

Colors
0054AA
0677BA
7BADD7
CADEEF
E8F1F8

Requirements
Must have
• use current theme of our website www.pellisterjourneys.com.au. Keep simple and effective.
Nice to have
• use one image that I have provided
Should not have
• multiple graphics

```html
<!DOCTYPE html>
<html lang="en">
<head>
<meta charset="utf-8">
<title>Pellister Journeys – 40 Years Banners</title>
<link rel="stylesheet" href="https://fonts.googleapis.com/css2?family=Bebas+Neue&family=Montserrat:wght@700;800&family=Poppins:wght@400&display=swap">
<style>
  :root {
    --board: #2673b2;
    --board-light: #2f82c0;
    --navy: #04173d;
    --brand-blue: #2389d9;
    --accent-blue: #3593e6;
    --ribbon: #f05a2a;
    --ribbon-fold: #a63512;
    --paper: #ffffff;
    --label: #ffffff;
  }
  html, body {
    margin: 0;
    width: 1200px;
    height: 1200px;
    overflow: hidden;
  }
  body {
    position: relative;
    background: radial-gradient(circle at 50% 55%, var(--board-light) 0%, var(--board) 70%);
    font-family: "Montserrat", sans-serif;
  }
  .board-label {
    position: absolute;
    left: 600px;
    transform: translateX(-50%);
    margin: 0;
    font-family: "Poppins", sans-serif;
    font-weight: 400;
    font-size: 18px;
    letter-spacing: 0.5px;
    color: var(--label);
  }
  .banner {
    position: absolute;
    left: 275px;
    width: 650px;
    height: 150px;
    background: var(--paper);
    box-shadow: 0 10px 28px rgba(0, 20, 60, 0.35);
    overflow: hidden;
  }
  .banner svg { display: block; width: 650px; height: 150px; }
  .banner--one   { top: 215px; }
  .banner--two   { top: 525px; }
  .banner--three { top: 835px; }
  .display { font-family: "Bebas Neue", sans-serif; fill: var(--paper); }
  .brand-name { font-family: "Montserrat", sans-serif; font-weight: 800; font-size: 16px; fill: var(--navy); }
  .web { font-family: "Montserrat", sans-serif; font-weight: 700; font-size: 11px; fill: var(--navy); }
  .tag-year { fill: var(--accent-blue); }
</style>
</head>
<body>

<p class="board-label" style="top:178px;">BANNER-1</p>
<p class="board-label" style="top:488px;">BANNER-2</p>
<p class="board-label" style="top:798px;">BANNER-3</p>

<!-- Banner 1 -->
<div class="banner banner--one">
  <svg viewBox="0 0 650 150" xmlns="http://www.w3.org/2000/svg">
    <defs>
      <linearGradient id="photo-traveller" x1="0" y1="0" x2="1" y2="1">
        <stop offset="0" stop-color="#efe6d8"/>
        <stop offset="0.5" stop-color="#c9a583"/>
        <stop offset="1" stop-color="#6f4a34"/>
      </linearGradient>
    </defs>
    <circle cx="596" cy="66" r="164" fill="var(--brand-blue)"/>
    <g role="img" aria-label="Photo of a traveller walking through an airport terminal with a suitcase">
      <circle cx="600" cy="60" r="152" fill="url(#photo-traveller)"/>
    </g>
    <circle cx="368" cy="75" r="136" fill="var(--brand-blue)"/>
    <circle cx="360" cy="75" r="130" fill="var(--navy)"/>
    <text class="brand-name" x="16" y="36">Pellister Journeys</text>
    <rect x="16" y="86" width="46" height="18" rx="9" fill="var(--brand-blue)"/>
    <text class="display" x="39" y="101" font-size="15" text-anchor="middle">VISIT</text>
    <path d="M66 90 Q77 90 79 102 M75 99 L79 103 L82 98" fill="none" stroke="var(--brand-blue)" stroke-width="1.4" stroke-linecap="round"/>
    <g fill="none" stroke="var(--navy)" stroke-width="1">
      <circle cx="22" cy="122" r="5.5"/><ellipse cx="22" cy="122" rx="2.5" ry="5.5"/><line x1="16.5" y1="122" x2="27.5" y2="122"/>
    </g>
    <text class="web" x="32" y="126">www.pellisterjourneys.com.au</text>
    <text class="display" x="292" y="40" font-size="20" text-anchor="middle">CELEBRATE</text>
    <text class="display" x="292" y="128" font-size="104" text-anchor="middle">40</text>
    <g transform="rotate(13 334 63)">
      <polygon points="296,68 304,68 304,80" fill="var(--ribbon-fold)"/>
      <polygon points="296,52 372,52 366,63 372,74 296,74" fill="var(--ribbon)"/>
      <text class="display" x="331" y="70" font-size="20" text-anchor="middle" font-style="italic">YEARS</text>
    </g>
    <text class="display" x="340" y="108" font-size="16">SERVICE THROUGH</text>
    <text class="display" x="340" y="126" font-size="16">EXPERIENCE SINCE 1983</text>
  </svg>
</div>

<!-- Banner 2 -->
<div class="banner banner--two">
  <svg viewBox="0 0 650 150" xmlns="http://www.w3.org/2000/svg">
    <defs>
      <linearGradient id="photo-business" x1="0" y1="0" x2="1" y2="1">
        <stop offset="0" stop-color="#dfe9ee"/>
        <stop offset="0.55" stop-color="#9aa7ab"/>
        <stop offset="1" stop-color="#7b5334"/>
      </linearGradient>
    </defs>
    <circle cx="596" cy="66" r="164" fill="var(--brand-blue)"/>
    <g role="img" aria-label="Photo of a business traveller checking her phone beside an airport window with a leather bag">
      <circle cx="600" cy="60" r="152" fill="url(#photo-business)"/>
    </g>
    <circle cx="368" cy="75" r="136" fill="var(--brand-blue)"/>
    <circle cx="360" cy="75" r="130" fill="var(--navy)"/>
    <text class="brand-name" x="16" y="36">Pellister Journeys</text>
    <rect x="16" y="86" width="46" height="18" rx="9" fill="var(--brand-blue)"/>
    <text class="display" x="39" y="101" font-size="15" text-anchor="middle">VISIT</text>
    <path d="M66 90 Q77 90 79 102 M75 99 L79 103 L82 98" fill="none" stroke="var(--brand-blue)" stroke-width="1.4" stroke-linecap="round"/>
    <g fill="none" stroke="var(--navy)" stroke-width="1">
      <circle cx="22" cy="122" r="5.5"/><ellipse cx="22" cy="122" rx="2.5" ry="5.5"/><line x1="16.5" y1="122" x2="27.5" y2="122"/>
    </g>
    <text class="web" x="32" y="126">www.pellisterjourneys.com.au</text>
    <text class="display" x="292" y="40" font-size="20" text-anchor="middle">CELEBRATE</text>
    <text class="display" x="292" y="128" font-size="104" text-anchor="middle">40</text>
    <g transform="rotate(13 334 63)">
      <polygon points="296,68 304,68 304,80" fill="var(--ribbon-fold)"/>
      <polygon points="296,52 372,52 366,63 372,74 296,74" fill="var(--ribbon)"/>
      <text class="display" x="331" y="70" font-size="20" text-anchor="middle" font-style="italic">YEARS</text>
    </g>
    <text class="display" x="340" y="108" font-size="16" font-style="italic">SERVICE THROUGH</text>
    <text class="display" x="340" y="126" font-size="16" font-style="italic">EXPERIENCE SINCE <tspan class="tag-year">1983</tspan></text>
  </svg>
</div>

<!-- Banner 3 -->
<div class="banner banner--three">
  <svg viewBox="0 0 650 150" xmlns="http://www.w3.org/2000/svg">
    <defs>
      <linearGradient id="photo-team" x1="0" y1="0" x2="1" y2="1">
        <stop offset="0" stop-color="#eef3f7"/>
        <stop offset="0.5" stop-color="#c7b3a0"/>
        <stop offset="1" stop-color="#4f6f8f"/>
      </linearGradient>
    </defs>
    <circle cx="596" cy="66" r="164" fill="var(--brand-blue)"/>
    <g role="img" aria-label="Photo of a cheerful travel team working together at a laptop in a bright office">
      <circle cx="600" cy="60" r="152" fill="url(#photo-team)"/>
    </g>
    <circle cx="368" cy="75" r="136" fill="var(--brand-blue)"/>
    <circle cx="360" cy="75" r="130" fill="var(--navy)"/>
    <text class="brand-name" x="16" y="36">Pellister Journeys</text>
    <rect x="16" y="86" width="46" height="18" rx="9" fill="var(--brand-blue)"/>
    <text class="display" x="39" y="101" font-size="15" text-anchor="middle">VISIT</text>
    <path d="M66 90 Q77 90 79 102 M75 99 L79 103 L82 98" fill="none" stroke="var(--brand-blue)" stroke-width="1.4" stroke-linecap="round"/>
    <g fill="none" stroke="var(--navy)" stroke-width="1">
      <circle cx="22" cy="122" r="5.5"/><ellipse cx="22" cy="122" rx="2.5" ry="5.5"/><line x1="16.5" y1="122" x2="27.5" y2="122"/>
    </g>
    <text class="web" x="32" y="126">www.pellisterjourneys.com.au</text>
    <text class="display" x="292" y="40" font-size="20" text-anchor="middle">CELEBRATE</text>
    <text class="display" x="292" y="128" font-size="104" text-anchor="middle">40</text>
    <g transform="rotate(13 334 63)">
      <polygon points="296,68 304,68 304,80" fill="var(--ribbon-fold)"/>
      <polygon points="296,52 372,52 366,63 372,74 296,74" fill="var(--ribbon)"/>
      <text class="display" x="331" y="70" font-size="20" text-anchor="middle" font-style="italic">YEARS</text>
    </g>
    <text class="display" x="340" y="108" font-size="16" font-style="italic">SERVICE THROUGH</text>
    <text class="display" x="340" y="126" font-size="16" font-style="italic">EXPERIENCE SINCE <tspan class="tag-year">1983</tspan></text>
  </svg>
</div>

</body>
</html>
```